New Company Website

Need a new website for my company Marlow Greenery.
Marlow Greenery offers four business lines: Interior Landscaping, Urbanscaping, Holiday Decorating, and Rental Plants.
Interior Landscaping is the interior installation and maintenance of live plants and flowers in corporate offices. Interiorscape contracts will be for a variety of terms from month to month to 3 years with differing price points in each option.
Urbanscaping refers to landscaping in the urban environment and is restricted in this definition to street side planters and medians, monument plantings and rooftop/balcony gardens.
Holiday Decorating is the Christmas/Hanukkah decorating during the winter season for corporate offices. The model for this business is to lease decorations for a period of 3 years.
Plant rentals is the short term rental of plants and live flowers (orchids, kalanchoe, etc) to event venues. The long term plan is to become the exclusive interior plant vendor for tradeshow organizations in the Tri-State area.

Target Market(s)

Office Managers, Building Managers, Event Coordinators

Industry/Entity Type

Landscaping

Requirements
Must have
• I love my logo. Please incorporate and use colors. Do not change logo.
Nice to have
• These are my competitors:
www.leafhollowdesigns.example
www.verdalo.example

```html
<!DOCTYPE html>
<html lang="en">
<head>
<meta charset="utf-8">
<title>Marlow Greenery</title>
<link href="https://fonts.googleapis.com/css2?family=Ubuntu:wght@300;400;500;700&display=swap" rel="stylesheet">
<style>
:root{
  --green:#3dbb2c;
  --green-dark:#2fa321;
  --blue:#0b5aa6;
  --navy:#08397a;
  --text:#6b6b6b;
  --grey-bg:#f3f3f3;
  --field:#f5f5f5;
  --field-line:#d9d9d9;
}
*{margin:0;padding:0;box-sizing:border-box}
html,body{width:782px;height:1200px;overflow:hidden}
body{background:var(--grey-bg);font-family:"Ubuntu",sans-serif;color:var(--text);position:relative}
.page{position:absolute;left:78px;top:0;width:627px;height:1010px;background:#fff;box-shadow:0 0 6px rgba(0,0,0,.12)}
.abs{position:absolute}
.brand{left:84px;top:14px;width:130px;height:84px}
.brand-mark{position:absolute;left:34px;top:2px;width:50px;height:50px;border-radius:50%;background:var(--blue)}
.brand-name{position:absolute;left:0;top:60px;font-weight:700;font-size:14px;color:var(--blue);white-space:nowrap}
.call{right:84px;top:64px;text-align:right}
.call-label{font-weight:300;font-size:17px;color:#8a8a8a}
.call-number{font-size:18px;color:var(--blue);margin-top:2px}
.nav{left:84px;top:113px;width:614px;height:43px;background:linear-gradient(#46c634,#33aa24);display:flex}
.nav a{display:flex;align-items:center;justify-content:center;color:#fff;font-family:"Ubuntu",sans-serif;font-weight:500;font-size:9px;letter-spacing:.1px;text-decoration:none;border-right:1px solid rgba(255,255,255,.35);height:100%}
.nav a.active{background:linear-gradient(#0d4c95,#08346f)}
.search{left:554px;top:126px;width:134px;height:17px;background:#fff;border:1px solid #cfe8c8;font-size:5px;color:#aaa;padding:5px 6px}
.search svg{position:absolute;right:4px;top:3px}
.hero{left:84px;top:165px;width:614px;height:231px;background:linear-gradient(#8fbde6 0%,#c7dcea 22%,#6e9a4a 45%,#4f8f2c 70%,#5aa332 100%)}
.hero-title{left:98px;top:338px;font-weight:300;font-size:28px;color:#fff}
.dots{left:99px;top:377px;display:flex;gap:3px}
.dots i{width:8px;height:8px;border-radius:50%;background:#fff}
.dots i:first-child{background:var(--navy)}
.section-title{font-family:"Ubuntu",sans-serif;font-size:11.5px;color:var(--blue);font-weight:500}
.services-title{left:0;width:782px;top:420px;text-align:center}
.card{top:450px;width:143px;min-height:229px;display:flex;flex-direction:column}
.card .thumb{height:84px;flex:none}
.card h3{font-weight:400;font-size:9.5px;color:var(--blue);margin-top:10px}
.card p{font-size:7px;line-height:15.5px;margin-top:3px;text-align:justify}
.btn{margin-top:auto;width:60px;height:22px;flex:none;background:var(--green);color:#fff;font-size:7.5px;font-weight:500;display:flex;align-items:center;justify-content:center;border-radius:2px}
.col-title{top:725px}
.news{left:85px;top:762px;width:195px}
.news p{font-size:7px;line-height:15.6px;text-align:justify}
.news .date{color:var(--blue);font-size:7.5px;margin:3px 0 16px}
.portrait{left:299px;top:757px;width:76px;height:76px;border-radius:50%;background:linear-gradient(#9a8a7a,#4a4040);border:2px solid #333}
.person{left:381px;top:778px}
.person-name{font-size:12px;color:var(--blue)}
.person-role{font-size:7px;color:#333;margin-top:3px}
.quote{left:300px;top:842px;width:182px;font-size:7px;line-height:15.6px;text-align:justify}
.field{left:503px;width:194px;background:var(--field);border:1px solid var(--field-line);font-size:7px;color:#aaa;padding:10px 6px;border-radius:2px}
.send{left:629px;top:954px;width:66px;height:23px;background:var(--blue);color:#fff;font-size:9.5px;font-weight:500;display:flex;align-items:center;justify-content:center;border-radius:2px}
.footer{left:0;top:1010px;width:782px;height:190px;background:var(--green)}
.f-col{top:1030px;color:#fff}
.f-col h4{font-size:9px;font-weight:500;margin-bottom:10px}
.f-col li{list-style:none;font-size:7.5px;line-height:15.7px}
.f-col p{font-size:7px;line-height:14.5px;width:146px;text-align:justify}
.f-field{position:absolute;left:0;width:145px;height:18px;background:#fff;border:1px solid #cfe8c8;font-size:6.5px;color:#888;padding:4px 5px}
.subscribe{position:absolute;left:82px;top:110px;width:63px;height:15px;background:var(--blue);color:#fff;font-size:7.5px;border-radius:8px;display:flex;align-items:center;justify-content:center}
.social{position:absolute;left:0;width:89px;height:18px;display:flex;align-items:center;justify-content:space-between}
.social i{width:18px;height:18px;border-radius:50%;background:#fff}
.social span{font-size:7.5px}
.copyright{left:0;width:782px;top:1174px;text-align:center;color:#fff;font-size:7.5px;padding-left:34px}
</style>
</head>
<body>
<div class="page"></div>

<div class="abs brand">
  <span class="brand-mark"></span>
  <span class="brand-name">Marlow Greenery</span>
</div>

<div class="abs call">
  <div class="call-label">Call Toll Free</div>
  <div class="call-number">1-888-555-0142</div>
</div>

<nav class="abs nav">
  <a class="active" style="width:74px">HOME</a>
  <a style="width:74px">ABOUT US</a>
  <a style="width:76px">SERVICES</a>
  <a style="width:98px">TESTIMONIALS</a>
  <a style="width:59px">FAQ'S</a>
  <a style="width:79px;border-right:0">CONTACT US</a>
</nav>
<div class="abs search">Type search
  <svg width="8" height="8" viewBox="0 0 8 8"><circle cx="3.2" cy="3.2" r="2.4" fill="none" stroke="#999" stroke-width="1"/><line x1="5" y1="5" x2="7.5" y2="7.5" stroke="#999" stroke-width="1.2"/></svg>
</div>

<div class="abs hero" role="img" aria-label="Large yellow house with manicured lawn, trees and flower beds under a blue sky"></div>
<div class="abs hero-title">Landscaping</div>
<div class="abs dots"><i></i><i></i><i></i><i></i></div>

<h2 class="abs section-title services-title">OUR SERVICES</h2>

<div class="abs card" style="left:84px">
  <div class="thumb" role="img" aria-label="Grey house with garden and trees" style="background:linear-gradient(#a9c9e6,#8a9aa0 50%,#4e7f34)"></div>
  <h3>Landscaping</h3>
  <p>Interior Landscaping is the interior installation and maintenance of live plants and flowers in corporate offices. Interiorscape contracts will be for a variety of terms from month to month to 3 years with differing price points in each option.</p>
  <span class="btn">Read More</span>
</div>
<div class="abs card" style="left:242px">
  <div class="thumb" role="img" aria-label="Aerial view of a green city with towers" style="background:linear-gradient(#c9d6d8,#8aa190 45%,#5d7f45)"></div>
  <h3>Urbanscaping</h3>
  <p>Urbanscaping refers to landscaping in the urban environment and is restricted in this definition to street side planters and medians, monument plantings and rooftop/balcony gardens.</p>
  <span class="btn">Read More</span>
</div>
<div class="abs card" style="left:400px">
  <div class="thumb" role="img" aria-label="Living room decorated for the holidays with a tree and fireplace" style="background:linear-gradient(#c9a37a,#8a4a2a 55%,#5a2418)"></div>
  <h3>Holiday Decorating</h3>
  <p>Is the Christmas/Hanukkah decorating during the winter season for corporate offices. The model for this business is to lease decorations for a period of 3 years.</p>
  <span class="btn">Read More</span>
</div>
<div class="abs card" style="left:554px">
  <div class="thumb" role="img" aria-label="Pink flowers on a wooden deck" style="background:linear-gradient(120deg,#3f6e2a,#c54a6e 45%,#b9b1a3)"></div>
  <h3>Rental Plants</h3>
  <p>Plant rentals is the short term rental of plants and live flowers (orchids, kalanchoe, etc) to event venues</p>
  <span class="btn">Read More</span>
</div>

<h2 class="abs section-title col-title" style="left:85px">LATEST NEWS</h2>
<h2 class="abs section-title col-title" style="left:293px">TESTIMONIALS</h2>
<h2 class="abs section-title col-title" style="left:502px">CONTACT US</h2>

<div class="abs news">
  <p>Lorem Ipsum is simply dummy text of the printing and typesetting industry. Lorem Ipsum has been the industry's standard dummy text ever since the 1500s</p>
  <div class="date">Date 22-11-2013 &nbsp;GST &nbsp;22:10</div>
  <p>It has survived not only five centuries, but also the leap into electronic typesetting, remaining unchanged.</p>
  <div class="date">Date 22-11-2013 &nbsp;GST &nbsp;22:10</div>
  <p>It was popularised in the 1960s with the release of Typeleaf sheets containing Lorem Ipsum passages, and more recently with desktop publishing software like Quillset Pager including versions of Lorem Ipsum.</p>
  <div class="date">Date 22-11-2013 &nbsp;GST &nbsp;22:10</div>
</div>

<div class="abs portrait" role="img" aria-label="Portrait photo of the company executive"></div>
<div class="abs person">
  <div class="person-name">Daniel Hartley</div>
  <div class="person-role">CEO, Executive Member</div>
</div>
<p class="abs quote">Lorem ipsum dolor sit amet, consectetur adipisicing elit, sed do eiusmod tempor incididunt ut labore et dolore magna aliqua. Ut enim ad minim veniam, quis nostrud exercitation ullamco laboris nisi ut aliquip ex ea commodo consequat. Duis aute irure dolor in reprehenderit in voluptate velit esse cillum dolore eu fugiat nulla pariatur. Excepteur sint occaecat cupidatat non proident, sunt in culpa qui officia deserunt mollit anim id est laborum.</p>

<div class="abs field" style="top:766px;height:27px">Name</div>
<div class="abs field" style="top:804px;height:27px">E-mail</div>
<div class="abs field" style="top:843px;height:27px">Phone</div>
<div class="abs field" style="top:882px;height:66px">Comments</div>
<div class="abs send">SEND</div>

<footer class="abs footer"></footer>
<div class="abs f-col" style="left:85px">
  <h4>Quick Links</h4>
  <ul><li>Home</li><li>About Us</li><li>Services</li><li>Testimonials</li><li>Faq's</li><li>Contact Us</li></ul>
</div>
<div class="abs f-col" style="left:242px">
  <h4>Support Links</h4>
  <ul><li>Legal Notice</li><li>Privacy Policy</li><li>Terms &amp; Conditions</li><li>Help</li></ul>
</div>
<div class="abs f-col" style="left:399px;width:146px;height:130px">
  <h4>Newsletter SignUp</h4>
  <p>Sign-up for our daily emails by entering your information below:</p>
  <div class="f-field" style="top:58px">Name</div>
  <div class="f-field" style="top:85px">Enter Your E-Mail ID</div>
  <span class="subscribe">Subscribe</span>
</div>
<div class="abs f-col" style="left:607px;width:89px;height:110px">
  <h4>Connect With Us</h4>
  <div class="social" style="top:24px"><i></i><span>Chirper</span></div>
  <div class="social" style="top:49px"><i></i><span>Friendbook</span></div>
  <div class="social" style="top:73px"><i></i><span>Worklink</span></div>
</div>
<div class="abs copyright">Copyright ©2013 Company Name &nbsp;- All rights reserved</div>
</body>
</html>
```